WordPress Site Design and Code for Technology Consulting Startup

We need a WordPress design and code to a new site on Nimbo Vault. We have the logo and colors ready. The site will be a brochure site with a CONTACT page that contains a form that the prospective client fills out. The other pages would be ABOUT / SERVICES (3 option drop-down) / SUPPORT. The site should be appropriate for an IT Consulting / IT Managed Services / IT Project Management services in the Chicago area.

Target Market(s)

Across small, medium, large businesses.

Industry/Entity Type

Technology, network infrastructure, IT.

Coding

Coded - Design and coding required

Number of Pages Required

5+ page

Requirements
Nice to have
• I prefer mid-modern / simple / art deco / minimalist.

```html
<!DOCTYPE html>
<html lang="en">
<head>
<meta charset="utf-8">
<title>Nimbo Vault – IT Consulting &amp; Managed Services</title>
<link href="https://fonts.googleapis.com/css2?family=Montserrat:wght@400;600;700&family=Open+Sans:ital,wght@0,400;0,600;1,400&display=swap" rel="stylesheet">
<style>
:root{
  --navy:#1d2736;
  --navy-2:#26334a;
  --orange:#f39200;
  --teal:#1c9db3;
  --ink:#2d3440;
  --muted:#8a919c;
  --line:#e4e7eb;
  --soft:#f5f6f8;
  --white:#ffffff;
}
*{box-sizing:border-box;margin:0;padding:0}
html,body{width:1200px;height:3256px;overflow:hidden}
body{font-family:"Open Sans",Arial,sans-serif;font-size:12px;color:var(--ink);background:var(--white);position:relative}
h1,h2,h3,h4,.heading{font-family:"Montserrat",Arial,sans-serif}
.wrap{width:960px;margin:0 auto;position:relative}
.ph{display:block}
p{line-height:1.7;color:var(--muted)}

/* top bar */
.topbar{height:28px;background:var(--navy);color:#aab3c0;font-size:10px}
.topbar .wrap{display:flex;justify-content:space-between;align-items:center;height:28px}
.topbar .social{display:flex;gap:8px}
.topbar .social span{width:10px;height:10px;border-radius:50%;background:#56627a}

/* header */
.header{height:72px;background:var(--white)}
.header .wrap{display:flex;align-items:center;justify-content:space-between;height:72px}
.brand{display:flex;align-items:center;gap:8px;font-family:"Montserrat",sans-serif;font-weight:700;font-size:24px;color:var(--navy);letter-spacing:1px}
.brand i{width:22px;height:22px;background:var(--orange);display:block}
.contacts{display:flex;gap:34px}
.contact{display:flex;gap:8px;align-items:center;font-size:10px;color:var(--muted)}
.contact b{display:block;color:var(--ink);font-size:11px}
.contact svg{width:22px;height:22px}

/* hero */
.hero{position:relative;height:480px;background:linear-gradient(120deg,#3a4657 0%,#5b6675 45%,#8d8f92 100%)}
.hero::after{content:"";position:absolute;inset:0;background:rgba(20,28,40,.45)}
.nav{position:absolute;top:0;left:120px;width:960px;height:34px;background:var(--navy);z-index:2;display:flex;justify-content:space-between}
.nav ul{list-style:none;display:flex}
.nav li{padding:0 18px;line-height:34px;font-family:"Montserrat",sans-serif;font-weight:600;font-size:10px;color:#fff}
.nav li.active{background:var(--orange)}
.nav .cta{background:var(--orange);color:#fff;font-family:"Montserrat",sans-serif;font-weight:700;font-size:10px;padding:0 22px;line-height:34px}
.hero-copy{position:absolute;z-index:2;left:480px;top:176px;width:600px;color:#fff}
.hero-copy h1{font-size:34px;line-height:1.25;font-weight:700}
.hero-copy p{color:#dfe3e8;margin-top:14px;font-size:12px}
.btns{display:flex;gap:12px;margin-top:22px}
.btn{display:inline-block;padding:9px 22px;font-family:"Montserrat",sans-serif;font-weight:700;font-size:10px;color:#fff;background:var(--orange)}
.btn.alt{background:transparent;border:1px solid #fff}

/* services */
.services{height:468px;background:var(--soft);padding-top:52px}
.intro{display:flex;gap:40px;align-items:flex-start}
.intro h2{width:200px;text-align:right;font-size:17px;line-height:1.3;color:var(--navy);border-right:3px solid var(--orange);padding-right:18px}
.intro p{width:460px}
.cards{display:grid;grid-template-columns:1fr 1fr;gap:20px 40px;margin-top:50px}
.card{background:#fff;display:flex;gap:16px;padding:12px;height:110px;border:1px solid var(--line)}
.card .ph{width:120px;height:86px;background:linear-gradient(135deg,#7a8796,#c9ced3)}
.card h3{font-size:13px;color:var(--navy);margin-bottom:6px}
.card p{font-size:10.5px;line-height:1.6}

/* about */
.about{height:320px;display:flex}
.about .ph{width:600px;height:320px;background:linear-gradient(120deg,#8f8676,#c9c2b2);position:relative}
.badge{position:absolute;right:-30px;top:26px;background:var(--teal);color:#fff;font-family:"Montserrat",sans-serif;font-weight:700;font-size:18px;padding:12px 22px}
.about-copy{flex:1;background:var(--navy);color:#fff;padding:40px 120px 0 70px}
.about-copy h2{font-size:20px}
.rule{width:40px;height:3px;background:var(--orange);margin:10px 0 14px}
.about-copy p{color:#aab3c0;font-size:11px;margin-bottom:10px}
.feats{display:flex;gap:40px;margin-top:16px}
.feat{display:flex;gap:8px;align-items:center;font-size:11px;color:#fff}
.feat svg{width:26px;height:26px}

/* testimonials + values */
.values{height:392px;padding-top:46px}
.values .wrap{display:flex;gap:80px}
.testi{width:320px}
.sec-title{font-size:18px;color:var(--navy)}
.person{display:flex;gap:12px;align-items:center;margin:14px 0}
.avatar{width:56px;height:56px;border-radius:50%;background:linear-gradient(135deg,#b39a85,#7c6a5d)}
.person b{font-size:12px;color:var(--navy);display:block}
.stars{color:var(--orange);font-size:11px}
.dots{display:flex;gap:5px;margin-top:14px}
.dots span{width:7px;height:7px;border-radius:50%;background:#cfd3d8}
.dots span:first-child{background:var(--orange)}
.vals{flex:1;position:relative}
.tabs{display:flex;margin:14px 0 16px;border-bottom:1px solid var(--line);width:380px}
.tabs div{flex:1;text-align:center;padding:8px 0;font-size:10px;font-weight:600;color:var(--muted)}
.tabs .on{background:var(--teal);color:#fff}
.vals h4{font-size:12px;color:var(--navy);margin-bottom:6px}
.vals p{width:380px;font-size:11px}
.checks{display:grid;grid-template-columns:190px 190px;gap:6px 0;margin-top:12px;list-style:none;font-size:11px}
.checks li{display:flex;gap:6px;align-items:center}
.checks svg{width:11px;height:11px;flex:none}
.vals .ph{position:absolute;right:0;top:40px;width:170px;height:200px;background:linear-gradient(135deg,#e3e5e8,#b9bec4)}

/* small business */
.small{height:212px;display:flex}
.small .ph{width:520px;height:212px;background:linear-gradient(120deg,#5d6571,#a5a9ad)}
.small-copy{flex:1;background:var(--navy-2);padding:34px 120px 0 50px;color:#fff}
.small-copy h2{font-size:16px}
.small-copy p{color:#aab3c0;font-size:11px;margin:8px 0 12px}
.small-copy .checks{grid-template-columns:repeat(3,170px);color:#dbe0e6}

/* stats */
.stats{height:140px;background:var(--teal)}
.stats .wrap{display:flex;height:140px;align-items:center}
.stat{flex:1;display:flex;align-items:center;gap:10px;color:#fff;padding-left:30px;border-left:1px solid rgba(255,255,255,.3)}
.stat:first-child{border-left:0}
.stat b{font-family:"Montserrat",sans-serif;font-size:34px}
.stat span{font-size:10px;line-height:1.3;text-transform:uppercase}

/* advisors */
.advisors{height:388px;padding-top:42px}
.team{display:grid;grid-template-columns:repeat(4,1fr);gap:20px;margin-top:24px}
.member .ph{height:210px;background:linear-gradient(180deg,#d9dde2,#aeb5bd)}
.member .tag{background:var(--teal);color:#fff;text-align:center;padding:8px 0}
.member .tag b{font-family:"Montserrat",sans-serif;font-size:11px;display:block}
.member .tag span{font-size:9px;opacity:.85}

/* partners + contact */
.split{height:408px;padding-top:34px;position:relative}
.split .wrap{display:flex;gap:40px}
.partners{width:440px}
.partners p{font-size:11px;margin:12px 0 20px}
.logos{display:grid;grid-template-columns:repeat(3,1fr);gap:18px}
.logos .mark{height:48px;display:flex;align-items:center;justify-content:center}
.logos .mark span{width:60px;height:28px;background:#cdd1d6;display:block}
.logos .mark span.c{width:34px;height:34px;border-radius:50%}
.touch{flex:1;position:relative}
.touch .ph{position:absolute;right:-120px;top:-34px;width:420px;height:408px;background:linear-gradient(135deg,#f7f8f9,#dde1e5)}
.form{position:relative;margin-top:18px;width:260px}
.field{height:28px;border:1px solid var(--line);background:#fff;margin-bottom:8px;font-size:10px;color:var(--muted);padding:7px 10px}
.field.area{height:60px}

/* query band */
.query{height:52px;background:var(--teal)}
.query .wrap{display:flex;justify-content:center;align-items:center;gap:30px;height:52px}
.query em{color:#fff;font-size:15px}

/* footer */
.footer{height:256px;background:var(--navy);padding-top:40px;color:#aab3c0}
.footer .wrap{display:flex;gap:50px}
.fcol h4{color:#fff;font-size:12px;margin-bottom:14px}
.fcol ul{list-style:none;font-size:10.5px;line-height:2.2}
.about-f{width:230px}
.about-f p{font-size:10.5px;color:#aab3c0;margin:12px 0}
.about-f .brand{color:#fff;font-size:20px}
.phone-f{color:var(--orange);font-weight:700;font-size:13px}
.gallery{display:grid;grid-template-columns:repeat(3,54px);gap:6px}
.gallery span{height:44px;background:linear-gradient(135deg,#5b6677,#8c96a3)}
.copyright{height:40px;background:#161e2a;color:#7f8896;font-size:10px}
.copyright .wrap{display:flex;justify-content:space-between;align-items:center;height:40px}
</style>
</head>
<body>

<div class="topbar"><div class="wrap"><span>Welcome to Nimbo Vault consulting and support services</span><div class="social"><span></span><span></span><span></span><span></span></div></div></div>

<header class="header"><div class="wrap">
  <div class="brand"><i></i>NIMBO VAULT</div>
  <div class="contacts">
    <div class="contact"><svg viewBox="0 0 24 24"><path d="M3 6h18v12H3z M3 6l9 7 9-7" fill="none" stroke="#f39200" stroke-width="1.6"/></svg><div><b>info@nimbovault.com</b>Email us anytime</div></div>
    <div class="contact"><svg viewBox="0 0 24 24"><path d="M6 3l4 4-2 3c1 3 3 5 6 6l3-2 4 4-3 3C10 21 3 14 3 6z" fill="#f39200"/></svg><div><b>+1 (312) 555-0148</b>Call for support</div></div>
    <div class="contact"><svg viewBox="0 0 24 24"><circle cx="12" cy="12" r="9" fill="none" stroke="#f39200" stroke-width="1.6"/><path d="M12 7v5l3 3" fill="none" stroke="#f39200" stroke-width="1.6"/></svg><div><b>Mon - Sat 8 - 6 PM</b>Sunday closed</div></div>
  </div>
</div></header>

<section class="hero" role="img" aria-label="Photo of a team working together at laptops in a bright office">
  <nav class="nav"><ul><li class="active">HOME</li><li>ABOUT US</li><li>SERVICES</li><li>SUPPORT</li><li>CONTACT US</li></ul><span class="cta">FREE SUPPORT</span></nav>
  <div class="hero-copy">
    <h1>Seamless IT Solutions That Work Overtime So You Don't Have To</h1>
    <p>Dependable managed IT services and expert consulting for growing teams across Chicago. We keep networks secure, systems running and your people focused on the work that matters.</p>
    <div class="btns"><span class="btn">READ MORE</span><span class="btn alt">VIEW MORE</span></div>
  </div>
</section>

<section class="services"><div class="wrap">
  <div class="intro">
    <h2>WE OFFER<br>DIFFERENT SERVICES</h2>
    <p>From first audit to round-the-clock monitoring, our consultants plan, deploy and support the technology your business depends on. Every engagement is shaped around your goals, your budget and the pace of your growth.</p>
  </div>
  <div class="cards">
    <div class="card"><span class="ph" role="img" aria-label="Photo of server hardware"></span><div><h3>Managed IT Services</h3><p>Proactive monitoring, patching and helpdesk support that keeps every device and user productive.</p></div></div>
    <div class="card"><span class="ph" role="img" aria-label="Photo of a planning meeting"></span><div><h3>Project Management</h3><p>Clear timelines and steady delivery for migrations, rollouts and infrastructure upgrades.</p></div></div>
    <div class="card"><span class="ph" role="img" aria-label="Photo of a consultant at a desk"></span><div><h3>IT Consulting</h3><p>Practical advice on networks, cloud and security from engineers who know your industry.</p></div></div>
    <div class="card"><span class="ph" role="img" aria-label="Photo of a laptop with charts"></span><div><h3>Digital Solutions</h3><p>Modern tools and workflows that connect your team and simplify daily operations.</p></div></div>
  </div>
</div></section>

<section class="about">
  <div class="ph" role="img" aria-label="Photo of colleagues reviewing work on a laptop"><span class="badge">Est. 2013</span></div>
  <div class="about-copy">
    <h2>Who We Are</h2><div class="rule"></div>
    <p>Nimbo Vault is a Chicago technology partner helping businesses of every size run reliable, secure and well-planned IT. Our team blends hands-on engineering with clear communication.</p>
    <p>We stay with you from the first conversation to the last ticket, so your systems grow as fast as your ambitions.</p>
    <div class="feats">
      <div class="feat"><svg viewBox="0 0 24 24"><circle cx="9" cy="8" r="3.5" fill="none" stroke="#f39200" stroke-width="1.6"/><path d="M2 20c0-4 3-6 7-6s7 2 7 6" fill="none" stroke="#f39200" stroke-width="1.6"/></svg>Dedicated<br>Team</div>
      <div class="feat"><svg viewBox="0 0 24 24"><path d="M12 3l2.6 5.6 6 .7-4.5 4.1 1.2 6L12 16.4 6.7 19.4l1.2-6L3.4 9.3l6-.7z" fill="none" stroke="#f39200" stroke-width="1.6"/></svg>Best<br>Advisors</div>
      <div class="feat"><svg viewBox="0 0 24 24"><circle cx="12" cy="12" r="9" fill="none" stroke="#f39200" stroke-width="1.6"/><path d="M12 7v5l3 3" fill="none" stroke="#f39200" stroke-width="1.6"/></svg>24/7<br>Supports</div>
    </div>
  </div>
</section>

<section class="values"><div class="wrap">
  <div class="testi">
    <h2 class="sec-title">Testimonials</h2><div class="rule"></div>
    <div class="person"><span class="avatar" role="img" aria-label="Client portrait"></span><div><b>Dan Ortiz</b><span class="stars">★★★★★</span></div></div>
    <p>Their team took over our network during a busy season and nothing slipped. Response times are fast, the reports are clear and we finally have a plan for the next three years.</p>
    <div class="dots"><span></span><span></span><span></span><span></span></div>
  </div>
  <div class="vals">
    <h2 class="sec-title">Our Company Values</h2><div class="rule"></div>
    <div class="tabs"><div class="on">Quality</div><div>Commitment</div><div>Success</div></div>
    <h4>Our Company Quality</h4>
    <p>We measure success by uptime, security and the confidence our clients feel every working day.</p>
    <ul class="checks">
      <li><svg viewBox="0 0 12 12"><path d="M2 6l3 3 5-6" fill="none" stroke="#f39200" stroke-width="1.8"/></svg>Fast Response Time</li>
      <li><svg viewBox="0 0 12 12"><path d="M2 6l3 3 5-6" fill="none" stroke="#f39200" stroke-width="1.8"/></svg>Certified Engineers</li>
      <li><svg viewBox="0 0 12 12"><path d="M2 6l3 3 5-6" fill="none" stroke="#f39200" stroke-width="1.8"/></svg>Clear Reporting</li>
      <li><svg viewBox="0 0 12 12"><path d="M2 6l3 3 5-6" fill="none" stroke="#f39200" stroke-width="1.8"/></svg>Secure Systems</li>
      <li><svg viewBox="0 0 12 12"><path d="M2 6l3 3 5-6" fill="none" stroke="#f39200" stroke-width="1.8"/></svg>Customer Satisfaction</li>
      <li><svg viewBox="0 0 12 12"><path d="M2 6l3 3 5-6" fill="none" stroke="#f39200" stroke-width="1.8"/></svg>Fair Pricing</li>
    </ul>
    <span class="ph" role="img" aria-label="Photo of a calculator and paperwork"></span>
  </div>
</div></section>

<section class="small">
  <div class="ph" role="img" aria-label="Photo of a small business owner at work"></div>
  <div class="small-copy">
    <h2>WE HELPING SMALL BUSINESS</h2>
    <p>Enterprise-grade support sized for small teams, with simple plans and one number to call.</p>
    <ul class="checks">
      <li><svg viewBox="0 0 12 12"><path d="M2 6l3 3 5-6" fill="none" stroke="#f39200" stroke-width="1.8"/></svg>Audit &amp; Assessment</li>
      <li><svg viewBox="0 0 12 12"><path d="M2 6l3 3 5-6" fill="none" stroke="#f39200" stroke-width="1.8"/></svg>Network Security</li>
      <li><svg viewBox="0 0 12 12"><path d="M2 6l3 3 5-6" fill="none" stroke="#f39200" stroke-width="1.8"/></svg>Cloud Backup</li>
      <li><svg viewBox="0 0 12 12"><path d="M2 6l3 3 5-6" fill="none" stroke="#f39200" stroke-width="1.8"/></svg>Business Services</li>
      <li><svg viewBox="0 0 12 12"><path d="M2 6l3 3 5-6" fill="none" stroke="#f39200" stroke-width="1.8"/></svg>Device Management</li>
      <li><svg viewBox="0 0 12 12"><path d="M2 6l3 3 5-6" fill="none" stroke="#f39200" stroke-width="1.8"/></svg>Strategic Planning</li>
    </ul>
  </div>
</section>

<section class="stats"><div class="wrap">
  <div class="stat"><b>12</b><span>Years of<br>Experience</span></div>
  <div class="stat"><b>54</b><span>Professional<br>Advisors</span></div>
  <div class="stat"><b>40</b><span>Projects<br>Done</span></div>
  <div class="stat"><b>89</b><span>Happy<br>Clients</span></div>
</div></section>

<section class="advisors"><div class="wrap">
  <h2 class="sec-title">Meet Our Advisors</h2><div class="rule"></div>
  <div class="team">
    <div class="member"><div class="ph" role="img" aria-label="Advisor portrait"></div><div class="tag"><b>EMMA RUIZ</b><span>Senior Consultant</span></div></div>
    <div class="member"><div class="ph" role="img" aria-label="Advisor portrait"></div><div class="tag"><b>NOAH KENT</b><span>Network Engineer</span></div></div>
    <div class="member"><div class="ph" role="img" aria-label="Advisor portrait"></div><div class="tag"><b>LIAM FORD</b><span>Project Manager</span></div></div>
    <div class="member"><div class="ph" role="img" aria-label="Advisor portrait"></div><div class="tag"><b>SARA BLOOM</b><span>Support Lead</span></div></div>
  </div>
</div></section>

<section class="split"><div class="wrap">
  <div class="partners">
    <h2 class="sec-title">Our Partners</h2><div class="rule"></div>
    <p>We work alongside trusted vendors and local firms to deliver complete, well-supported technology solutions for every client we serve.</p>
    <div class="logos">
      <div class="mark"><span></span></div><div class="mark"><span class="c"></span></div><div class="mark"><span></span></div>
      <div class="mark"><span class="c"></span></div><div class="mark"><span></span></div><div class="mark"><span class="c"></span></div>
    </div>
  </div>
  <div class="touch">
    <span class="ph" role="img" aria-label="Faint photo of a desk with documents"></span>
    <h2 class="sec-title" style="position:relative">Get in Touch</h2><div class="rule" style="position:relative"></div>
    <div class="form">
      <div class="field">Your Name</div>
      <div class="field">Your Email</div>
      <div class="field">Subject</div>
      <div class="field area">Your Message</div>
      <span class="btn">SUBMIT NOW</span>
    </div>
  </div>
</div></section>

<section class="query"><div class="wrap"><em>If you have any querry for related investment ... We are available</em><span class="btn">CONTACT US</span></div></section>

<footer class="footer"><div class="wrap">
  <div class="about-f">
    <div class="brand"><i></i>NIMBO VAULT</div>
    <p>Managed IT, consulting and project delivery for businesses across the Chicago area.</p>
    <div class="phone-f">+1 (312) 555-0148</div>
  </div>
  <div class="fcol"><h4>Our Services</h4><ul><li>Managed IT Services</li><li>Project Management</li><li>IT Consulting</li><li>Digital Solutions</li><li>Network Support</li></ul></div>
  <div class="fcol"><h4>&nbsp;</h4><ul><li>Cloud Backup</li><li>Security Audits</li><li>Help Desk</li><li>Hardware Setup</li><li>Training</li></ul></div>
  <div class="fcol"><h4>From our Gallery</h4><div class="gallery" role="img" aria-label="Gallery of office and team photos"><span></span><span></span><span></span><span></span><span></span><span></span></div></div>
</div></footer>
<div class="copyright"><div class="wrap"><span>© 2024 Nimbo Vault. All rights reserved.</span><span>Privacy · Terms</span></div></div>

</body>
</html>
```